Martin K Doyle DDS (dentist) needs a business card/business logo design

I would like an eye-catchingly conservative or elegant graphic presentation of my business name with the elements: prevention, restoration, and cosmetics (these are the services I'd like to emphasize) .
The business card would have room for address lines, phone and fax, web address. No standard teeth or oral representations please. Should communicate professionalism. Whatever color scheme works.

Thank you

Target Market(s)

I just want a good looking business card

Industry/Entity Type

Conservative

Contact Information for Business Card

Adress: 4173 Brisford Ave Lakewood CA 90716 Phone: 562 430 5926 FAX 562 430 6384 Web: Pinegrovedental.com

Font styles to use
Sans Serif

Colors
0255a3

Requirements
Must have
• business name with the elements: prevention, restoration, and cosmetics (these are the services I'd like to emphasize)
• communicates professionalism
Nice to have
• eye catching but not flashy graphics
Should not have
• no pictures of teeth or dental instruments

```html
<!DOCTYPE html>
<html lang="en">
<head>
<meta charset="utf-8">
<title>Martin K Doyle DDS — Business Card</title>
<link rel="stylesheet" href="https://fonts.googleapis.com/css2?family=Playfair+Display:wght@900&family=Roboto+Condensed:wght@300;400&display=swap">
<style>
  :root {
    --page: #e9e6e3;
    --maroon: #5a0f1e;
    --maroon-text: #7a1526;
    --ink: #1b1718;
    --white: #ffffff;
    --glitter-light: #f4ece6;
    --glitter-warm: #dcc3b6;
    --glitter-rose: #c9a49a;
    --band-tint: rgba(120, 62, 66, 0.32);
    --right-tint: rgba(255, 255, 255, 0.38);
  }
  * { margin: 0; padding: 0; box-sizing: border-box; }
  html, body { width: 1200px; height: 848px; overflow: hidden; background: var(--page); }
  .canvas { position: relative; width: 1200px; height: 848px; }
  .card {
    position: absolute; left: 100px; top: 138px; width: 1000px; height: 572px;
    overflow: hidden; box-shadow: 0 10px 30px rgba(0,0,0,0.18);
  }
  .card-backdrop {
    position: absolute; inset: 0;
    background:
      radial-gradient(ellipse at 25% 70%, var(--glitter-light) 0%, transparent 60%),
      radial-gradient(ellipse at 60% 30%, var(--glitter-rose) 0%, transparent 65%),
      linear-gradient(170deg, #e7ddd8 0%, var(--glitter-warm) 45%, var(--glitter-light) 100%);
  }
  .service-band { position: absolute; left: 440px; top: 0; width: 260px; height: 458px; background: var(--band-tint); }
  .light-panel { position: absolute; left: 700px; top: 0; width: 300px; height: 458px; background: var(--right-tint); }
  .identity { position: absolute; left: 110px; top: 72px; }
  .practitioner {
    font-family: "Playfair Display", Georgia, serif; font-weight: 900;
    font-size: 44px; line-height: 1; color: var(--ink); white-space: nowrap;
  }
  .credential { color: var(--maroon-text); }
  .services {
    font-family: "Roboto Condensed", Arial, sans-serif; font-weight: 400;
    font-size: 22px; line-height: 1.2; color: var(--maroon-text); margin-top: 6px; margin-left: 14px; white-space: nowrap;
  }
  .contact {
    position: absolute; left: 480px; top: 178px; list-style: none;
    font-family: "Roboto Condensed", Arial, sans-serif; font-weight: 400;
    font-size: 26px; line-height: 1.3; color: var(--ink); white-space: nowrap;
  }
  .contact li { display: flex; align-items: flex-start; gap: 14px; margin-bottom: 8px; }
  .contact svg { flex: none; width: 22px; height: 22px; margin-top: 6px; fill: var(--ink); }
  .web-band {
    position: absolute; left: 0; bottom: 0; width: 1000px; height: 114px; background: var(--maroon);
    display: flex; align-items: center; padding-left: 110px; gap: 20px;
  }
  .web-band svg { width: 38px; height: 38px; }
  .web-address {
    font-family: "Roboto Condensed", Arial, sans-serif; font-weight: 300;
    font-size: 40px; color: var(--white); letter-spacing: 0.5px;
  }
</style>
</head>
<body>
<main class="canvas">
  <article class="card">
    <div class="card-backdrop" role="img" aria-label="Soft-focus champagne and rose glitter bokeh background"></div>
    <div class="service-band"></div>
    <div class="light-panel"></div>

    <header class="identity">
      <h1 class="practitioner">Martin K Doyle, <span class="credential">DDS</span></h1>
      <p class="services">prevention, restoration, and cosmetics</p>
    </header>

    <ul class="contact">
      <li>
        <svg viewBox="0 0 24 24" aria-label="Phone"><path d="M6.6 10.8a15.2 15.2 0 0 0 6.6 6.6l2.2-2.2a1 1 0 0 1 1-.25 11.4 11.4 0 0 0 3.6.57 1 1 0 0 1 1 1V20a1 1 0 0 1-1 1A17 17 0 0 1 3 4a1 1 0 0 1 1-1h3.5a1 1 0 0 1 1 1 11.4 11.4 0 0 0 .57 3.6 1 1 0 0 1-.25 1z"/></svg>
        <span>562-430-5926</span>
      </li>
      <li>
        <svg viewBox="0 0 24 24" aria-label="Fax"><path d="M6 2h9l3 3v5H6z M8 4v4h8V6h-2V4z M3 11h18a1 1 0 0 1 1 1v8a1 1 0 0 1-1 1H3a1 1 0 0 1-1-1v-8a1 1 0 0 1 1-1z M6 15v2h12v-2z"/></svg>
        <span>562-430-6384</span>
      </li>
      <li>
        <svg viewBox="0 0 24 24" aria-label="Address"><path d="M12 2a7 7 0 0 0-7 7c0 5.2 7 13 7 13s7-7.8 7-13a7 7 0 0 0-7-7zm0 9.5A2.5 2.5 0 1 1 12 6.5a2.5 2.5 0 0 1 0 5z"/></svg>
        <span>4173 Brisford Ave.<br>Lakewood, CA 90716</span>
      </li>
    </ul>

    <footer class="web-band">
      <svg viewBox="0 0 40 40" aria-label="Website">
        <circle cx="20" cy="20" r="18" fill="#ffffff"/>
        <g fill="none" stroke="#5a0f1e" stroke-width="2">
          <ellipse cx="20" cy="20" rx="8" ry="17"/>
          <line x1="3" y1="20" x2="37" y2="20"/>
          <path d="M6 11h28M6 29h28"/>
        </g>
      </svg>
      <span class="web-address">Pinegrovedental.com</span>
    </footer>
  </article>
</main>
</body>
</html>
```